TRUCK WASH OUTDOOR DRIVE THROUGH MENU CONTEST

WE NEED A DRIVE THROUGH MENU WITH OUR SERVICES AND PRICES. I HAVE ATTACHED A FEW EXAMPLES THAT I STARTED.

I WANT THIS TO BE EYE CATCHING WITH BRIGHT COLORS

Target Market(s)

TRUCK WASH AND DETAIL SHOP, TRANSPORTATION.

Requirements
Must have
• INCORPORATE MY LOGO INTO THE SIGN.
• FINAL PROJECT MUST BE IN .AI FORMAT.
• COMPANY COLORS ARE RED AND BLUE

```html
<!DOCTYPE html>
<html lang="en">
<head>
<meta charset="UTF-8">
<title>Rig Bath Co. – Drive Through Menu</title>
<link href="https://fonts.googleapis.com/css2?family=Poppins:wght@500;600&display=swap" rel="stylesheet">
<style>
  :root {
    --page: #ffffff;
    --red: #ee0234;
    --red-deep: #d2002b;
    --red-fold: #8f001c;
    --band: #0a6aa1;
    --aqua: #27b3dc;
    --aqua-light: #3bbce3;
    --aqua-dark: #1a9fd2;
    --ink-light: #ffffff;
  }
  * { margin: 0; padding: 0; box-sizing: border-box; }
  html, body { width: 1200px; height: 621px; overflow: hidden; background: var(--page); }
  body { font-family: "Poppins", sans-serif; }

  .menu-board {
    position: relative;
    width: 1200px;
    height: 621px;
    background: var(--page);
  }
  .board-panel {
    position: absolute;
    left: 42px; top: 54px;
    width: 1116px; height: 512px;
    overflow: hidden;
    background: var(--red);
  }
  .board-panel .backdrop { position: absolute; inset: 0; }

  .brand-name {
    position: absolute;
    left: 0; right: 0; top: 105px;
    text-align: center;
    font-weight: 600;
    font-size: 54px;
    letter-spacing: 1px;
    color: var(--aqua);
  }

  .package {
    position: absolute;
    top: 230px;
    width: 248px; height: 248px;
    border-radius: 50%;
    background: radial-gradient(circle at 50% 65%, var(--aqua-light), var(--aqua) 60%, var(--aqua-dark));
    box-shadow: 0 4px 10px rgba(0, 40, 80, 0.35);
    color: var(--ink-light);
    text-align: center;
  }
  .package.express  { left: 28px; }
  .package.silver   { left: 298px; }
  .package.gold     { left: 567px; }
  .package.platinum { left: 834px; }

  .package-name {
    margin-top: 84px;
    font-weight: 500;
    font-size: 44px;
    line-height: 1;
    letter-spacing: 0.5px;
  }
  .package-services {
    margin-top: 12px;
    font-weight: 600;
    font-size: 16.5px;
    line-height: 23px;
  }

  .price-tag {
    position: absolute;
    top: 16px; right: -4px;
    width: 112px; height: 58px;
  }
  .price-tag svg { position: absolute; inset: 0; }
  .price-tag .price {
    position: absolute;
    left: 12px; right: 6px; top: 0; height: 48px;
    display: flex; align-items: center; justify-content: center;
    font-weight: 600;
    font-size: 26px;
    color: var(--ink-light);
  }
</style>
</head>
<body>
<main class="menu-board">
  <section class="board-panel">
    <svg class="backdrop" width="1116" height="512" viewBox="0 0 1116 512" aria-hidden="true">
      <defs>
        <filter id="dome-shadow" x="-10%" y="-10%" width="120%" height="120%">
          <feDropShadow dx="0" dy="0" stdDeviation="8" flood-color="#7a0018" flood-opacity="0.45"/>
        </filter>
      </defs>
      <rect width="1116" height="512" fill="var(--red)"/>
      <ellipse cx="558" cy="120" rx="560" ry="500" fill="var(--red-deep)" filter="url(#dome-shadow)"/>
      <rect x="0" y="262" width="1116" height="186" fill="var(--band)"/>
    </svg>

    <h1 class="brand-name">Rig Bath Co.</h1>

    <article class="package express">
      <div class="price-tag">
        <svg viewBox="0 0 112 58" aria-hidden="true">
          <polygon points="102,48 112,48 112,58" fill="var(--red-fold)"/>
          <polygon points="0,0 112,0 112,48 0,48 12,24" fill="var(--red)"/>
        </svg>
        <span class="price">$50</span>
      </div>
      <h2 class="package-name">express</h2>
      <p class="package-services">pre-soak, soap,rinse</p>
    </article>

    <article class="package silver">
      <div class="price-tag">
        <svg viewBox="0 0 112 58" aria-hidden="true">
          <polygon points="102,48 112,48 112,58" fill="var(--red-fold)"/>
          <polygon points="0,0 112,0 112,48 0,48 12,24" fill="var(--red)"/>
        </svg>
        <span class="price">$100</span>
      </div>
      <h2 class="package-name">silver</h2>
      <p class="package-services">pre-soak, soap&amp;scrub,<br>rinse, tire shine</p>
    </article>

    <article class="package gold">
      <div class="price-tag">
        <svg viewBox="0 0 112 58" aria-hidden="true">
          <polygon points="102,48 112,48 112,58" fill="var(--red-fold)"/>
          <polygon points="0,0 112,0 112,48 0,48 12,24" fill="var(--red)"/>
        </svg>
        <span class="price">$150</span>
      </div>
      <h2 class="package-name">gold</h2>
      <p class="package-services">pre-soak, soap&amp;scrub,<br>rinse, tire shine,<br>wet x polish</p>
    </article>

    <article class="package platinum">
      <div class="price-tag">
        <svg viewBox="0 0 112 58" aria-hidden="true">
          <polygon points="102,48 112,48 112,58" fill="var(--red-fold)"/>
          <polygon points="0,0 112,0 112,48 0,48 12,24" fill="var(--red)"/>
        </svg>
        <span class="price">$150</span>
      </div>
      <h2 class="package-name">platinum</h2>
      <p class="package-services">pre-soak, soap&amp;scrub,<br>rinse, tire shine,<br>platinum protect</p>
    </article>
  </section>
</main>
</body>
</html>
```